Structural Engineering Business Card

Veltrow Drafts does residential house plans for clients in Lakewood Valley. Would like simple but elegant business card that is appropriate for a house plan engineering company. Prefer black business card with black/white them but open to other shades of blue. I uploaded a sample card that I came across that looked good but please come up with your own creative designs.

Contact Information for Business Card

Name, Title, Phone, Email, Address, website

```html
<!DOCTYPE html>
<html lang="en">
<head>
<meta charset="UTF-8">
<title>Veltrow Drafts – Business Card</title>
<link href="https://fonts.googleapis.com/css2?family=Outfit:wght@400;600;800&display=swap" rel="stylesheet">
<style>
  :root {
    --page-bg: #ececec;
    --card-dark: #000000;
    --card-light: #ffffff;
    --text-light: #ffffff;
    --text-dark: #000000;
    --silver: #b9b9b9;
  }
  * { box-sizing: border-box; margin: 0; padding: 0; }
  html, body {
    width: 1200px; height: 1200px; overflow: hidden;
    background: var(--page-bg);
    font-family: "Outfit", sans-serif;
  }
  .canvas { position: relative; width: 1200px; height: 1200px; }
  .card {
    position: absolute; left: 160px; width: 880px; height: 515px;
    box-shadow: 0 3px 10px rgba(0,0,0,0.18);
    overflow: hidden;
  }
  .card--front { top: 65px; background: var(--card-dark); color: var(--text-light); }
  .card--back { top: 622px; background: var(--card-light); color: var(--text-dark); }

  .brand-name {
    position: absolute; font-weight: 800; text-transform: uppercase;
    letter-spacing: 0.5px; white-space: nowrap; line-height: 1;
  }
  .card--front .brand-name {
    right: 70px; top: 98px; font-size: 56px; color: var(--silver);
  }
  .card--back .brand-name {
    left: 0; right: 0; top: 218px; text-align: center;
    font-size: 74px; color: var(--text-dark);
  }

  .person { position: absolute; right: 70px; top: 262px; text-align: right; }
  .person__name { font-size: 28px; font-weight: 600; letter-spacing: 0.3px; }
  .person__title { font-size: 21px; font-weight: 400; margin-top: 4px; letter-spacing: 0.4px; }

  .contact { position: absolute; right: 70px; top: 362px; list-style: none; }
  .contact__item {
    display: flex; justify-content: flex-end; align-items: center; gap: 12px;
    font-size: 20px; letter-spacing: 0.4px; height: 34px;
  }
  .contact__icon { width: 13px; height: 13px; fill: var(--text-light); flex: none; }

  .step-line { position: absolute; left: 0; top: 340px; width: 450px; height: 130px; }
</style>
</head>
<body>
<div class="canvas">
  <section class="card card--front">
    <div class="brand-name">Veltrow Drafts</div>

    <div class="person">
      <div class="person__name">Marcus T Delorien</div>
      <div class="person__title">President</div>
    </div>

    <ul class="contact">
      <li class="contact__item">0123456789
        <svg class="contact__icon" viewBox="0 0 24 24"><path d="M6.6 10.8a15.1 15.1 0 0 0 6.6 6.6l2.2-2.2a1 1 0 0 1 1-.25 11.4 11.4 0 0 0 3.6.57 1 1 0 0 1 1 1V20a1 1 0 0 1-1 1A17 17 0 0 1 3 4a1 1 0 0 1 1-1h3.5a1 1 0 0 1 1 1c0 1.25.2 2.45.57 3.57a1 1 0 0 1-.25 1z"/></svg>
      </li>
      <li class="contact__item">mailid@webmail.com
        <svg class="contact__icon" viewBox="0 0 24 24"><path d="M2 5h20v2l-10 7L2 7z"/><path d="M2 9l10 7 10-7v10H2z"/></svg>
      </li>
      <li class="contact__item">Lakewood Valley
        <svg class="contact__icon" viewBox="0 0 24 24"><path d="M12 2a7 7 0 0 0-7 7c0 5 7 13 7 13s7-8 7-13a7 7 0 0 0-7-7zm0 9.5A2.5 2.5 0 1 1 12 6.5a2.5 2.5 0 0 1 0 5z"/></svg>
      </li>
    </ul>

    <svg class="step-line" viewBox="0 0 450 130" aria-hidden="true">
      <defs>
        <linearGradient id="silverStroke" x1="0" y1="0" x2="1" y2="0">
          <stop offset="0" stop-color="#6f6f6f"/>
          <stop offset="0.4" stop-color="#f2f2f2"/>
          <stop offset="0.7" stop-color="#9a9a9a"/>
          <stop offset="1" stop-color="#d8d8d8"/>
        </linearGradient>
      </defs>
      <polyline points="0,5 224,5 224,120 446,120" fill="none" stroke="url(#silverStroke)" stroke-width="4"/>
    </svg>
  </section>

  <section class="card card--back">
    <div class="brand-name">Veltrow Drafts</div>
  </section>
</div>
</body>
</html>
```